Weihnachtskarte für überregionalen Mandantenkreis einer Unternehmensberatung
Zielgruppe
Die KOLVEN Steuerberatungsgesellschaft mbH ist überregional tätig und berät Kunden in steuerlichen und betriebswirtschaftlichen Belangen. Ein Tätigkeitsschwerpunkt unseres Unternehmens ist die steuerliche und betriebswirtschaftliche BEgleitung von Insolvenzverfahren im Auftrag renomierter Insolvenzverwalterkanzleien in Deutschland.
Aufgabenstellung
Die Weihnachtskarte sollte in einem puren, schlichten Look gehalten sein. Der Kreativität sind dabei keine Grenzen gesetzt. Wir können uns sowohl eher statische Muster/Grafiken als auch weihnachtliche Illustrationen vorstellen. Diese dürfen dann auch verspielt wirken, wobei dabei auch mit Kontrasten zu unserem klaren Corporate-Design gearbeitet werden sollte. Unsere Standardfarben in Firmenprsäentationen sind die folgenden Codes:
r149/g179/b215
r165/g164/b167
r195/g214/b155
und diverse Grautöne
Die Karte sollte folgende Inhalte besitzen:
1. Firmenschriftzug/Logo
Gesellschaftsname: KOLVEN Steuerberatungsgesellschaft mbH
2. Die Standorte unserer Gesellschaft
3. Kurzer Weihnachtsgruß, der so positioniert sein sollte, dass in dessen Umfeld Platz für einen handschriftlichen Gruß und eine Unterschrift bleibt
4. unsere Internetseite ("www.kolven-beispiel.de")
Als Anlage ist ein Datenblatt für die Erstellung der geeigneten Druckdatei beigefügt. Geplant ist die Karte im Format DIN lang (21x9,8), wobei die Nut an der Längsseite verlaufen soll. Der Karte wird dabei im Querformat bedruckt.

```html
<!DOCTYPE html>
<html lang="de">
<head>
<meta charset="utf-8">
<title>KOLVEN Weihnachtskarte</title>
<link rel="stylesheet" href="https://fonts.googleapis.com/css2?family=Source+Sans+3:ital,wght@0,400;0,600;1,400;1,600&family=Open+Sans:wght@400&display=swap">
<style>
  :root {
    --brand-blue: #2f5b9e;
    --ice-blue: #dbe5f0;
    --grey-top: #c8c8c8;
    --grey-fold: #e6e6e6;
    --fold-line: #6e6e6e;
    --card-edge: #9a9a9a;
    --paper: #ffffff;
    --quote-white: #ffffff;
  }
  * { margin: 0; padding: 0; box-sizing: border-box; }
  html, body { width: 1200px; height: 2293px; overflow: hidden; background: var(--paper); }
  body { position: relative; font-family: "Source Sans 3", sans-serif; }

  .card {
    position: absolute; left: 58px; width: 1054px; height: 1015px;
    border: 1px solid var(--card-edge); background: var(--paper); overflow: hidden;
  }
  .card--inside { top: 63px; }
  .card--outside { top: 1181px; height: 1012px; }

  .panel { position: absolute; left: 0; width: 100%; }
  .card--inside .panel--upper {
    top: 0; height: 507px;
    background: linear-gradient(to bottom, var(--grey-top), var(--grey-fold));
    border-bottom: 1px solid var(--fold-line);
  }
  .card--inside .panel--lower {
    top: 507px; height: 508px;
    background: linear-gradient(to bottom, #dcdcdc 0%, #f3f3f3 25%, var(--paper) 55%);
  }

  .quote { position: absolute; left: 0; top: 195px; width: 100%; text-align: center; color: var(--quote-white); }
  .quote__mark {
    position: absolute; font-family: "Source Sans 3", sans-serif; font-weight: 600; font-style: italic;
    font-size: 110px; line-height: 1; color: var(--quote-white); opacity: .9;
  }
  .quote__mark--open { left: 50px; top: 12px; }
  .quote__mark--close { right: 50px; top: -10px; }
  .quote__text { font-style: italic; font-size: 19.5px; padding-top: 20px; letter-spacing: -.2px; }
  .quote__author { font-style: italic; font-size: 12px; margin-top: 11px; }

  .greeting-text {
    position: absolute; top: 130px; left: 0; width: 100%; text-align: center;
    color: var(--brand-blue); font-size: 20px; line-height: 28.5px;
  }

  .card--outside .panel--upper { top: 0; height: 496px; border-bottom: 1px solid var(--fold-line); }
  .card--outside .panel--lower { top: 496px; height: 516px; }

  .back-info {
    position: absolute; left: 0; top: 18px; width: 100%; height: 160px;
    transform: rotate(180deg); text-align: center; color: var(--brand-blue);
    display: flex; flex-direction: column; justify-content: flex-start;
  }
  .back-info__company { font-family: "Open Sans", sans-serif; font-size: 12px; margin-top: 2px; }
  .back-info__locations { font-family: "Open Sans", sans-serif; font-size: 12px; line-height: 17px; margin-top: 22px; }
  .back-info__web { font-size: 21px; margin-top: 14px; }

  .decoration {
    position: absolute; left: 0; top: 20px; width: 100%; height: 496px;
    background:
      radial-gradient(ellipse 260px 230px at 230px 120px, rgba(219,229,240,.9), rgba(219,229,240,0) 70%),
      linear-gradient(to bottom, rgba(219,229,240,0) 0%, rgba(219,229,240,.55) 45%, rgba(219,229,240,.75) 100%);
  }
  .wordmark {
    position: absolute; right: 36px; top: 34px; display: flex; align-items: center; gap: 10px;
    font-family: "Source Sans 3", sans-serif; font-weight: 600; font-size: 30px; letter-spacing: 2px;
    color: var(--brand-blue);
  }
  .wordmark__square { width: 22px; height: 22px; background: var(--brand-blue); }

  .season-greeting { position: absolute; left: 0; top: 364px; width: 100%; text-align: center; color: var(--brand-blue); }
  .season-greeting__de { font-size: 20px; letter-spacing: .3px; }
  .season-greeting__en { font-style: italic; font-size: 36px; line-height: 1; margin-top: 1px; letter-spacing: -.3px; }
</style>
</head>
<body>
  <section class="card card--inside">
    <div class="panel panel--upper">
      <blockquote class="quote">
        <span class="quote__mark quote__mark--open">„</span>
        <p class="quote__text">Im Grunde sind es immer die Verbindungen mit Menschen, die dem Leben seinen Wert geben.</p>
        <p class="quote__author">Wilhelm von Harlstedt</p>
        <span class="quote__mark quote__mark--close">“</span>
      </blockquote>
    </div>
    <div class="panel panel--lower">
      <p class="greeting-text">
        In diesem Sinne bedanken wir uns herzlich für Ihr Vertrauen<br>
        und die angenehme Zusammenarbeit<br>
        und wünschen Ihnen ein besinnliches Weihnachtsfest<br>
        sowie ein erfolgreiches neues Jahr.
      </p>
    </div>
  </section>

  <section class="card card--outside">
    <div class="panel panel--upper">
      <div class="back-info">
        <p class="back-info__company">KOLVEN Steuerberatungsgesellschaft mbH</p>
        <p class="back-info__locations">
          Lindenallee 12 | 20100 Hamburg | T +49 40 0000001<br>
          Birkenweg 4 | 04100 Leipzig | T +49 341 0000002<br>
          Ahornstraße 9 | 80100 München | T +49 89 0000003<br>
          Eichenplatz 7 | 89000 Ulm | T +49 731 0000004
        </p>
        <p class="back-info__web">www.kolven-beispiel.de</p>
      </div>
    </div>
    <div class="panel panel--lower">
      <div class="decoration" role="img" aria-label="Zarter eisblauer Tannenzweig mit verblassten, überlagerten Schriftzügen „Merry Christmas and a Happy New Year“"></div>
      <div class="wordmark"><span>KOLVEN</span><span class="wordmark__square"></span></div>
      <div class="season-greeting">
        <p class="season-greeting__de">FROHE WEIHNACHTEN UND EIN GLÜCKLICHES NEUES JAHR</p>
        <p class="season-greeting__en">MERRY CHRISTMAS AND A HAPPY NEW YEAR</p>
      </div>
    </div>
  </section>
</body>
</html>
```